Velnor Kingsbridge Banner Designs

We are looking for 3 Graphic Banners that can be used on our Website and E-mail blasts to our membership base.
See attached file for more information

```html
<!DOCTYPE html>
<html lang="en">
<head>
<meta charset="utf-8">
<title>Velnor Kingsbridge Banner</title>
<link rel="stylesheet" href="https://fonts.googleapis.com/css2?family=Roboto:wght@500;700&display=swap">
<style>
  :root {
    --navy-deep: #1d2f73;
    --navy: #2a3f8f;
    --royal: #3a55b0;
    --haze: #5a70bd;
    --white: #ffffff;
    --panel: rgba(255, 255, 255, 0.16);
  }
  html, body {
    margin: 0;
    padding: 0;
    width: 1200px;
    height: 327px;
    overflow: hidden;
    background: var(--navy-deep);
  }
  .banner {
    position: relative;
    width: 1200px;
    height: 327px;
    overflow: hidden;
    font-family: "Roboto", Arial, sans-serif;
    color: var(--white);
  }
  .backdrop {
    position: absolute;
    inset: 0;
    background:
      radial-gradient(ellipse 420px 260px at 600px 200px, var(--haze) 0%, rgba(90,112,189,0) 100%),
      linear-gradient(180deg, var(--royal) 0%, var(--navy) 55%, var(--navy-deep) 100%);
  }
  .brand {
    position: absolute;
    left: 111px;
    top: 49px;
    display: flex;
    align-items: center;
  }
  .brand-mark {
    width: 131px;
    height: 58px;
    border-radius: 50%;
    background: var(--white);
    display: flex;
    align-items: center;
    justify-content: center;
    color: var(--navy);
    font-weight: 700;
    font-size: 26px;
  }
  .brand-text { margin-left: 6px; }
  .brand-title {
    margin: 0;
    font-size: 37px;
    font-weight: 700;
    line-height: 1;
  }
  .brand-tagline {
    margin: 8px 0 0;
    font-size: 14.5px;
    font-weight: 700;
  }
  .stats {
    position: absolute;
    left: 800px;
    top: 36px;
    width: 376px;
    height: 64px;
    border-radius: 4px;
    background: var(--panel);
    display: flex;
    justify-content: space-around;
    align-items: center;
    text-align: center;
    font-weight: 700;
    font-size: 14.5px;
    line-height: 27px;
  }
  .stat span { display: block; }
  .services {
    position: absolute;
    left: 0;
    top: 169px;
    width: 1200px;
    height: 120px;
    margin: 0;
    padding: 0;
    list-style: none;
  }
  .service {
    position: absolute;
    top: 0;
    width: 140px;
    margin-left: -70px;
    text-align: center;
  }
  .service-icon {
    display: block;
    height: 78px;
    margin: 0 auto;
  }
  .service-label {
    display: block;
    margin-top: 14px;
    font-size: 16px;
    font-weight: 700;
    line-height: 19px;
  }
</style>
</head>
<body>
<div class="banner">
  <div class="backdrop" role="img" aria-label="Blue-toned photograph of a parliament building with a clock tower, framed by faint maple leaves"></div>

  <div class="brand">
    <div class="brand-mark">Velnor</div>
    <div class="brand-text">
      <h1 class="brand-title">Global</h1>
      <p class="brand-tagline">Fostering Entrepreneurship Globally</p>
    </div>
  </div>

  <div class="stats">
    <div class="stat"><span>61</span><span>chapters</span></div>
    <div class="stat"><span>18</span><span>countries</span></div>
    <div class="stat"><span>11,261</span><span>members</span></div>
  </div>

  <ul class="services">
    <li class="service" style="left:167px">
      <svg class="service-icon" viewBox="0 0 90 78" width="90" height="78" aria-hidden="true">
        <rect x="4" y="3" width="82" height="54" rx="4" fill="none" stroke="#fff" stroke-width="6"/>
        <polyline points="20,42 36,24 52,34 70,18" fill="none" stroke="#fff" stroke-width="3"/>
        <circle cx="20" cy="42" r="4" fill="#fff"/><circle cx="36" cy="24" r="4" fill="#fff"/>
        <circle cx="52" cy="34" r="4" fill="#fff"/><circle cx="70" cy="18" r="4" fill="#fff"/>
        <path d="M33 60 h24 l6 14 h-36 z" fill="#fff"/>
      </svg>
      <span class="service-label">Mentoring</span>
    </li>
    <li class="service" style="left:380px">
      <svg class="service-icon" viewBox="0 0 78 78" width="78" height="78" aria-hidden="true">
        <line x1="39" y1="28" x2="39" y2="44" stroke="#fff" stroke-width="4"/>
        <line x1="39" y1="44" x2="18" y2="58" stroke="#fff" stroke-width="4"/>
        <line x1="39" y1="44" x2="60" y2="58" stroke="#fff" stroke-width="4"/>
        <circle cx="39" cy="15" r="12" fill="none" stroke="#fff" stroke-width="4"/>
        <circle cx="16" cy="62" r="12" fill="none" stroke="#fff" stroke-width="4"/>
        <circle cx="62" cy="62" r="12" fill="none" stroke="#fff" stroke-width="4"/>
        <circle cx="39" cy="12" r="4" fill="#fff"/><path d="M32 22 a7 6 0 0 1 14 0 z" fill="#fff"/>
        <circle cx="16" cy="59" r="4" fill="#fff"/><path d="M9 69 a7 6 0 0 1 14 0 z" fill="#fff"/>
        <circle cx="62" cy="59" r="4" fill="#fff"/><path d="M55 69 a7 6 0 0 1 14 0 z" fill="#fff"/>
      </svg>
      <span class="service-label">Networking</span>
    </li>
    <li class="service" style="left:594px">
      <svg class="service-icon" viewBox="0 0 100 78" width="100" height="78" aria-hidden="true">
        <polygon points="50,6 96,24 50,42 4,24" fill="#fff"/>
        <path d="M24 34 v22 q26 16 52 0 v-22 l-26 10 z" fill="#fff"/>
        <line x1="10" y1="26" x2="10" y2="54" stroke="#fff" stroke-width="2"/>
        <polygon points="7,54 13,54 10,66" fill="#fff"/>
      </svg>
      <span class="service-label">Education</span>
    </li>
    <li class="service" style="left:826px">
      <svg class="service-icon" viewBox="0 0 90 78" width="90" height="78" aria-hidden="true">
        <ellipse cx="46" cy="34" rx="20" ry="9" fill="#fff"/>
        <circle cx="58" cy="20" r="10" fill="#fff"/>
        <polygon points="67,16 76,20 67,23" fill="#fff"/>
        <path d="M5 36 l10 7 l10 -6 l10 7 l10 -7 l10 7 l10 -7 l10 6 l10 -7 a40 36 0 0 1 -80 0 z" fill="#fff"/>
      </svg>
      <span class="service-label">Incubating</span>
    </li>
    <li class="service" style="left:1050px">
      <svg class="service-icon" viewBox="0 0 90 78" width="90" height="78" aria-hidden="true">
        <circle cx="50" cy="10" r="9" fill="#fff"/>
        <ellipse cx="48" cy="44" rx="32" ry="24" fill="#fff"/>
        <rect x="8" y="34" width="14" height="14" rx="4" fill="#fff"/>
        <polygon points="26,26 30,12 40,24" fill="#fff"/>
        <rect x="26" y="60" width="10" height="14" rx="3" fill="#fff"/>
        <rect x="58" y="60" width="10" height="14" rx="3" fill="#fff"/>
        <path d="M79 40 q8 -2 6 -10" fill="none" stroke="#fff" stroke-width="3"/>
        <rect x="40" y="22" width="18" height="3" rx="1.5" fill="#2a3f8f"/>
      </svg>
      <span class="service-label">Funding</span>
    </li>
  </ul>
</div>
</body>
</html>
```